Sliders required for launch-to-market of broadband & telecoms provider

We require first of many sliders for launch-to-market of broadband & telecoms provider. We are looking for a unique colour scheme with high quality graphics. Please see attached images as to what we are looking for. We like the angled look as on banner image, but want a more brighter colour scheme. Glossy & hi res...

Industry/Entity Type

Telecommunications

Number of Pages Required

1 page

Colors

Designer to choose colors to be used in the design.

Requirements
Must have
• unique colour scheme and hi res images
Nice to have
• We like the angled look as on banner image, but want a more brighter/richer individual colour scheme. Glossy & hi res... as the colour will be our main colour used across site so can't just be standard colour. It needs to be unique to our brand.
Should not have
• boring colour scheme and low quality images

```html
<!DOCTYPE html>
<html lang="en">
<head>
<meta charset="UTF-8">
<title>Unlimited Broadband Slider</title>
<link rel="stylesheet" href="https://fonts.googleapis.com/css2?family=Black+Ops+One&family=Oswald:wght@600;700&family=Poppins:wght@500;600;700&display=swap">
<style>
  :root {
    --pink: #e6007f;
    --pink-side: #b8005f;
    --pink-deep: #7d0042;
    --orange: #f4a447;
    --scene-light: #f2f0ec;
    --scene-mid: #ddd6cc;
    --scene-warm: #c9ab92;
    --scene-cream: #e8ddd0;
    --white: #ffffff;
  }
  * { margin: 0; padding: 0; box-sizing: border-box; }
  html, body { width: 1200px; height: 720px; overflow: hidden; background: var(--white); }
  .slider {
    position: relative;
    width: 1200px;
    height: 720px;
    overflow: hidden;
  }
  .slider__photo {
    position: absolute;
    inset: 0;
    background:
      radial-gradient(ellipse 260px 420px at 250px 430px, var(--scene-warm) 0%, rgba(201,171,146,0.55) 55%, rgba(201,171,146,0) 100%),
      radial-gradient(ellipse 120px 130px at 220px 140px, #d9a98a 0%, rgba(217,169,138,0) 100%),
      radial-gradient(ellipse 260px 120px at 820px 620px, #f7f6f4 0%, rgba(247,246,244,0) 100%),
      linear-gradient(100deg, var(--scene-cream) 0%, var(--scene-mid) 45%, var(--scene-light) 100%);
  }
  .slider__backdrop {
    position: absolute;
    inset: 0;
    width: 1200px;
    height: 720px;
  }
  .slider__headline {
    position: absolute;
    left: 0;
    top: 0;
    width: 1200px;
    height: 240px;
  }
  .headline__text {
    font-family: "Black Ops One", "Oswald", sans-serif;
    font-weight: 400;
  }
  .price {
    position: absolute;
    left: 520px;
    top: 250px;
    color: var(--white);
    font-family: "Poppins", sans-serif;
  }
  .price__from {
    position: absolute;
    left: 62px;
    top: 0;
    font-size: 34px;
    font-weight: 600;
    line-height: 1;
  }
  .price__currency {
    position: absolute;
    left: 8px;
    top: 58px;
    font-size: 42px;
    font-weight: 700;
    line-height: 1;
  }
  .price__whole {
    position: absolute;
    left: 34px;
    top: 30px;
    font-size: 126px;
    font-weight: 700;
    line-height: 1;
    letter-spacing: -4px;
  }
  .price__cents {
    position: absolute;
    left: 172px;
    top: 52px;
    font-size: 46px;
    font-weight: 700;
    line-height: 1;
  }
  .price__period {
    position: absolute;
    left: 177px;
    top: 104px;
    font-size: 23px;
    font-weight: 500;
    line-height: 1;
    white-space: nowrap;
  }
  .cta {
    position: absolute;
    left: 515px;
    top: 422px;
    width: 322px;
    height: 65px;
    border-radius: 10px;
    background: var(--pink);
    color: var(--white);
    font-family: "Poppins", sans-serif;
    font-size: 27px;
    font-weight: 500;
    display: flex;
    align-items: center;
    justify-content: center;
    text-decoration: none;
  }
  .features {
    position: absolute;
    left: 0;
    top: 0;
    width: 1200px;
    height: 720px;
  }
  .feature__big {
    font-family: "Oswald", sans-serif;
    font-weight: 700;
    fill: var(--white);
  }
  .feature__small {
    font-family: "Oswald", sans-serif;
    font-weight: 600;
    fill: var(--white);
  }
  .feature__tiny {
    font-family: "Poppins", sans-serif;
    font-weight: 600;
    fill: var(--white);
    letter-spacing: 0.8px;
  }
</style>
</head>
<body>
<main class="slider">
  <div class="slider__photo" role="img" aria-label="Photo of a smiling young woman at a desk holding a mug, with a laptop and papers in a bright room"></div>

  <svg class="slider__backdrop" viewBox="0 0 1200 720" aria-hidden="true">
    <polygon points="0,0 1000,0 1000,545 0,295" fill="var(--orange)" opacity="0.78"/>
  </svg>

  <svg class="slider__headline" viewBox="0 0 1200 240">
    <text class="headline__text" x="515" y="110" textLength="435" lengthAdjust="spacingAndGlyphs" font-size="92" fill="var(--white)">UNLIMITIED</text>
    <text class="headline__text" x="355" y="228" textLength="600" lengthAdjust="spacingAndGlyphs" font-size="116" fill="var(--pink)">BROADBAND</text>
  </svg>

  <div class="price">
    <span class="price__from">from</span>
    <span class="price__currency">$</span>
    <span class="price__whole">18</span>
    <span class="price__cents">.99</span>
    <span class="price__period">a month</span>
  </div>

  <a class="cta" href="#offers">Check our offers &gt;</a>

  <svg class="features" viewBox="0 0 1200 720">
    <g class="feature">
      <polygon points="997,200 1150,200 1200,245 1047,245" fill="var(--pink-deep)"/>
      <polygon points="1150,45 1200,90 1200,245 1150,200" fill="var(--pink-side)"/>
      <rect x="997" y="45" width="153" height="155" fill="var(--pink)"/>
      <text class="feature__big" x="1070" y="95" text-anchor="middle" font-size="29">FIXED</text>
      <text class="feature__big" x="1070" y="137" text-anchor="middle" font-size="29">PRICE</text>
      <text class="feature__tiny" x="1070" y="162" text-anchor="middle" font-size="12">BROADBAND</text>
      <text class="feature__tiny" x="1070" y="179" text-anchor="middle" font-size="12">GUARANTEED</text>
    </g>
    <g class="feature">
      <polygon points="997,368 1150,368 1200,413 1047,413" fill="var(--pink-deep)"/>
      <polygon points="1150,215 1200,260 1200,413 1150,368" fill="var(--pink-side)"/>
      <rect x="997" y="215" width="153" height="153" fill="var(--pink)"/>
      <text class="feature__big" x="1072" y="272" text-anchor="middle" font-size="29">NO</text>
      <text class="feature__small" x="1070" y="305" text-anchor="middle" font-size="20">ACTIVATION</text>
      <text class="feature__small" x="1070" y="336" text-anchor="middle" font-size="20">FEE</text>
    </g>
    <g class="feature">
      <polygon points="997,540 1150,540 1200,585 1047,585" fill="var(--pink-deep)"/>
      <polygon points="1150,385 1200,430 1200,585 1150,540" fill="var(--pink-side)"/>
      <rect x="997" y="385" width="153" height="155" fill="var(--pink)"/>
      <text class="feature__big" x="1072" y="449" text-anchor="middle" font-size="29">18</text>
      <text class="feature__small" x="1072" y="482" text-anchor="middle" font-size="20">MONTH</text>
      <text class="feature__small" x="1072" y="513" text-anchor="middle" font-size="20">CONTRACT</text>
    </g>
  </svg>
</main>
</body>
</html>
```